Velora Lounge Duo Flyer - info and save 20%

We need a flyer designed around the look of our website - that retro feel - it can give some brief info on our duo and we need to present an offer of 20% off our normal prices for live music at private or corporate events and weddings.
Two hours $590 Now $472
Three hours $690 Now $ 552
Four hours $790 Now $632
Five hours $890 Now $712
About our duo:
Velora Duo - Live Jazz and Cocktail Music
Set the atmosphere with classy cocktail music and jazz at your next event of distinction. Marnie Holt on Piano and Gavin Thorley on the Bass - professional and dedicated musicians. All venues and all occasions. Servicing Brisbane & South-East Queensland. Acoustic or Electric - all venue sizes.
Testimonials:
Sat. March 21, 2013 | Fendrix Awards Dinner at the Palmvale Arts Centre
The Velora Duo provided the perfect entertainment for our Awards Dinner. It was fantastic to have the combination of purely background music and more upbeat music with vocals. Marnie was brilliant to deal with from the initial booking stage to the event and ensured that the entertainment option provided was the most suitable for our event.
Dana Whitcombe, Fendrix Pty Ltd
_______________________________________________________________________
Sat. June 26, 2012 | Wedding at the Riverbend Hall of Qld
We had Velora Duo play at our Cocktail Wedding Reception for the first couple of hours and they were simply delightful! The music was diverse, fun and great way to create a buzzing atmosphere while still having your guests being able to enjoy their conversations. As everyone knows weddings can be stressful but it was such a pleasure was dealing with Marnie Holt (pianist) of Velora Duo as she was completely helpful and professional in organising the music list and the arrangement and put our minds at rest knowing we were dealing with such professional and experienced musicians. It was a wonderful start to the evening and we had many complements on the wonderful music from our guests! It again completely reaffirmed to us how important good music is for creating a memorable experience on your wedding day and we cannot recommend Velora Duo and their pianist Marnie Holt enough!
Tessa & Martin, June 2012,
Fri. April 21st, 2011 | Surprise Birthday Party – Kestrel Club
You simply made the evening with your music. Thank you Velora Duo for another great night!”
Doyle Family 2011,
Fri. October 1st, 2010 - ongoing | Harbourview Manor, Queensland
It has been an absolute pleasure to have Marnie & Gavin perform for us at Harbourview Manor. Their love and passion for music is brought to life through their flawless performances and never cease to amaze myself or our guests with what they will come up with next. Marnie and Gavin are such wonderful characters who are willing to go above and beyond to support Harbourview Manor with whatever musical requests and repertoire we require.
Marnie has also been a fantastic help to me with the recommendation of other Brisbane based musicians whose professionalism and commitment to the music industry is faultless.
I would like to thank Marnie and Gavin and the Tidewave Sound team for their continuing musical support to Harbourview Manor.
Colleen Ashby - Assistant House Manager - Harbourview Manor Queensland
Updates
This project was meant to finish today - 25 Aug - I am not sure why it is saying that it has 7 more days to run - but we need it by tomorrow really !! (26 Aug)
This is a message from the printers re the design specs!
Design files> PDF settings. All CMYK colour settings no RGB.
Print ready files to have the noted minimum 3mm bleed design and the noted crop marks for final trim size.
1 up front, 1 up backs for cards or leaflets etc.

```html
<!DOCTYPE html>
<html lang="en">
<head>
<meta charset="utf-8">
<title>Velora Duo – Live Jazz and Cocktail Music – 20% Off</title>
<link rel="stylesheet" href="https://fonts.googleapis.com/css2?family=Josefin+Sans:wght@400;600;700&display=swap">
<style>
  :root {
    --page: #ffffff;
    --teal-deep: #86aaa7;
    --teal-light: #b3d1cc;
    --cream: #f4ecdb;
    --shadow-grey: #6d6d6d;
    --badge: #6f6f6f;
    --ink: #5a5a5a;
    --card: #f8f8f6;
  }
  * { margin: 0; padding: 0; box-sizing: border-box; }
  html, body {
    width: 1200px;
    height: 846px;
    overflow: hidden;
    background: var(--page);
  }
  .flyer {
    position: relative;
    width: 1200px;
    height: 846px;
    font-family: "Josefin Sans", "Futura", sans-serif;
  }
  .flyer__panel {
    position: absolute;
    left: 28px;
    top: 28px;
    width: 1146px;
    height: 788px;
    background: radial-gradient(ellipse 60% 55% at 48% 48%, var(--teal-light) 0%, var(--teal-deep) 100%);
    overflow: hidden;
  }
  .discount-badge {
    position: absolute;
    left: 68px;
    top: 132px;
    width: 162px;
    height: 162px;
    z-index: 2;
  }
  .discount-badge__label {
    position: absolute;
    inset: 0;
    display: flex;
    align-items: center;
    justify-content: center;
    color: #ffffff;
    font-weight: 700;
    font-size: 44px;
    padding-top: 6px;
  }
  .title {
    position: absolute;
    left: 234px;
    top: 104px;
    font-size: 112px;
    font-weight: 700;
    line-height: 1;
    letter-spacing: 0;
    color: var(--cream);
    text-shadow: 8px 5px 0 var(--shadow-grey);
    white-space: nowrap;
    z-index: 1;
  }
  .tagline {
    position: absolute;
    left: 496px;
    top: 236px;
    font-size: 31px;
    font-weight: 600;
    color: var(--ink);
    white-space: nowrap;
  }
  .intro {
    position: absolute;
    left: 218px;
    top: 310px;
    width: 446px;
    font-size: 16px;
    line-height: 22px;
    color: var(--cream);
  }
  .intro p + p { margin-top: 22px; }
  .price-card {
    position: absolute;
    left: 722px;
    top: 290px;
    width: 336px;
    height: 270px;
    background: var(--card);
    transform: rotate(-4deg);
    box-shadow: 4px 6px 14px rgba(40, 60, 60, 0.35);
    display: flex;
    flex-direction: column;
    justify-content: center;
    align-items: center;
    gap: 10px;
    padding-bottom: 40px;
  }
  .price-card__row {
    font-size: 22px;
    font-weight: 700;
    color: var(--ink);
    white-space: nowrap;
  }
  .website {
    position: absolute;
    left: 824px;
    top: 620px;
    font-size: 25px;
    color: var(--cream);
  }
</style>
</head>
<body>
  <main class="flyer">
    <section class="flyer__panel">
      <div class="discount-badge">
        <svg width="162" height="162" viewBox="0 0 162 162" aria-hidden="true">
          <circle cx="81" cy="81" r="81" fill="var(--badge)"/>
        </svg>
        <span class="discount-badge__label">-20%</span>
      </div>

      <h1 class="title">VELORA DUO</h1>
      <h2 class="tagline">Live Jazz and Cocktail Music</h2>

      <div class="intro">
        <p>Set the atmosphere with classy cocktail music and jazz at your next event of distinction. Marnie Holt on Piano and Gavin Thorley on the Bass - professional and dedicated musicians.</p>
        <p>All venues and all occasions. Servicing Brisbane &amp; South-East Queensland. Acoustic or Electric - all venue sizes.</p>
      </div>

      <div class="price-card">
        <p class="price-card__row">2 hours $590 Now $472</p>
        <p class="price-card__row">3 hours $690 Now $ 552</p>
        <p class="price-card__row">4 hours $790 Now $632</p>
        <p class="price-card__row">5 hours $890 Now $712</p>
      </div>

      <p class="website">veloraduomusic.com</p>
    </section>
  </main>
</body>
</html>
```